Verpackungsdesign für CBD-Öl
Zielgruppe
CBD Produkte
Aufgabenstellung
Erstellung eines Designs für eine Verpackung von CBD-Öl. Die Verpackung sollte sich von den üblichen CBD Verpackungen abheben, mit Logo,, Hintergrund und Farben meiner Webseite sollte gearbeitet werden siehe Foto.
Design sollte sehr edel und cool ausschauen, nicht wie die meisten CBD Verpackungen. Eure Kreativität könnt Ihr freien Lauf lassen. Wir lassen uns überraschen.
Größe der Faltschachtel: Länge 27 mm, Breite 28 mm, Höhe 90 mm
Erstellung eines Design für eine Faltschachtel mit 4 verschiedenen Inhaltsangaben.
Das Grunddesign der Verpackung ist immer das gleiche, nur die Inhaltsangabe an Cannabidiol variiert.
10 % 1000MG, 15 % 1500MG, 20 % 2000MG, 30 % 3000MG
Kornwiese sollte im Vordergrund stehen und der Hintergrund siehe Bild!
Was draufstehen sollte
Vegan & Glutenfrei
Vollspektrum
CBD Premium Hanföl
Nicht zum Verzehr geeignet
Duftöl
Siehe Bild von Sarn, die Inhaltsstoffe bitte freihalten, da wir unterschiedliche Inhaltsstoffe/ Geschmacksrichtungen haben.
Erstellung Design für das Etikett für die 10-ml-Flasche.
Größe Etikett: Länge: 85 mm, Höhe: 30 mm
Das Grunddesign für das Label der 10-ml-Flasche ist immer das gleiche. Jedoch auch hier variiert die Inhaltsangabe von Cannabidiol.
10% 15% 20% und 30%
Auch unser Firmenlogo KORNWIESE können wir Ihnen in anderen Größen senden.
Sie können uns auch schreiben, um weitere Fragen abzuklären.
Gutes designen.

```html
<!DOCTYPE html>
<html lang="de">
<head>
<meta charset="utf-8">
<title>KORNWIESE – Faltschachtel CBD Hanföl</title>
<link href="https://fonts.googleapis.com/css2?family=Oswald:wght@300;400&family=Ubuntu:wght@300;700&display=swap" rel="stylesheet">
<style>
  :root {
    --paper: #ffffff;
    --flap-black: #0c0c0e;
    --gold: #b8862a;
    --gold-light: #d6b15a;
    --tan: #d9b88a;
    --cream: #e9e2cc;
    --hemp-green: #5a8a3a;
    --eu-green: #8fbd1b;
    --white: #ffffff;
  }
  * { margin: 0; padding: 0; box-sizing: border-box; }
  html, body { width: 900px; height: 1200px; overflow: hidden; background: var(--paper); }
  .dieline { position: relative; width: 900px; height: 1200px; font-family: "Oswald", sans-serif; font-weight: 300; color: var(--gold); }
  .board { position: absolute; inset: 0; }
  .t { position: absolute; white-space: nowrap; letter-spacing: -0.3px; }
  .brand { position: absolute; font-family: "Oswald", sans-serif; font-weight: 400; color: var(--cream); letter-spacing: 2px; display: flex; align-items: center; gap: 8px; }
  .brand .dot { width: 10px; height: 10px; border-radius: 50%; background: var(--hemp-green); }
  .brand-top { left: 478px; top: 104px; font-size: 30px; }
  .brand-side { left: 16px; top: 598px; font-size: 28px; }
  .brand-vertical { position: absolute; left: 470px; top: 866px; transform-origin: 0 0; transform: rotate(-90deg); font-size: 76px; line-height: 1; color: var(--cream); font-weight: 400; letter-spacing: 11px; white-space: nowrap; }
  .notice { left: 253px; font-size: 21px; line-height: 28px; }
  .care { left: 249px; font-size: 16.5px; line-height: 22px; }
  .product-premium { left: 569px; top: 436px; font-family: "Ubuntu", sans-serif; font-weight: 700; font-size: 24px; color: var(--gold-light); }
  .product-cbd { left: 566px; top: 457px; font-family: "Ubuntu", sans-serif; font-weight: 700; font-size: 54px; color: var(--hemp-green); line-height: 1; }
  .product-oil { left: 569px; top: 510px; font-family: "Ubuntu", sans-serif; font-weight: 300; font-size: 33px; color: var(--tan); }
  .strength { left: 562px; top: 732px; font-family: "Ubuntu", sans-serif; font-weight: 700; font-size: 46px; color: var(--gold-light); }
  .spectrum { left: 564px; top: 790px; font-size: 18px; line-height: 25px; color: var(--tan); }
  .claim { left: 751px; font-size: 18px; }
  .bullets { position: absolute; left: 702px; top: 460px; list-style: none; font-size: 15.5px; line-height: 22px; }
  .bullets li::before { content: "•"; margin-right: 6px; font-size: 12px; }
  .ingredients { left: 701px; top: 704px; font-size: 16.5px; line-height: 22px; }
  .batch { left: 469px; font-size: 22px; color: var(--white); font-weight: 400; }
  .date-field { position: absolute; left: 463px; top: 1099px; width: 194px; height: 82px; background: var(--white); }
  .volume { left: 702px; top: 998px; font-size: 19px; color: var(--tan); }
</style>
</head>
<body>
<div class="dieline">
  <svg class="board" width="900" height="1200" viewBox="0 0 900 1200">
    <defs>
      <clipPath id="box-outline">
        <path d="M450,0 H677 V225 H900 V975 H677 V1200 H450 V975 H0 V225 H450 Z"/>
      </clipPath>
      <linearGradient id="board-shade" x1="0" y1="0" x2="1" y2="1">
        <stop offset="0" stop-color="#1a1a1b"/>
        <stop offset="0.45" stop-color="#333335"/>
        <stop offset="1" stop-color="#141415"/>
      </linearGradient>
      <linearGradient id="glow" x1="0" y1="1" x2="1" y2="0">
        <stop offset="0" stop-color="#e5b21c"/>
        <stop offset="0.4" stop-color="#f6c431"/>
        <stop offset="0.75" stop-color="#a4560d"/>
        <stop offset="1" stop-color="#3a1d06"/>
      </linearGradient>
      <linearGradient id="autumn-soft" x1="0" y1="0" x2="0" y2="1">
        <stop offset="0" stop-color="#9a5a1a" stop-opacity="0.55"/>
        <stop offset="1" stop-color="#b09a2a" stop-opacity="0.55"/>
      </linearGradient>
      <linearGradient id="green-soft" x1="0" y1="0" x2="0" y2="1">
        <stop offset="0" stop-color="#4f7d35" stop-opacity="0.5"/>
        <stop offset="1" stop-color="#d8cfae" stop-opacity="0.25"/>
      </linearGradient>
    </defs>
    <g clip-path="url(#box-outline)">
      <rect width="900" height="1200" fill="url(#board-shade)"/>
      <polygon points="0,440 900,860 900,975 0,620" fill="#111112" opacity="0.55"/>
      <polygon role="img" aria-label="Goldener Lichtstreifen" points="0,372 677,150 677,192 0,440" fill="url(#glow)" opacity="0.9"/>
      <rect x="450" y="975" width="227" height="225" fill="var(--flap-black)"/>
      <rect role="img" aria-label="Herbstliches Hanfblatt" x="0" y="683" width="102" height="168" rx="14" fill="url(#autumn-soft)"/>
    </g>
    <rect role="img" aria-label="Hanfblatt mit Lorbeerkranz" x="471" y="244" width="177" height="150" rx="18" fill="url(#green-soft)"/>
    <rect role="img" aria-label="Herbstliches Hanfblatt" x="477" y="874" width="171" height="101" rx="14" fill="url(#autumn-soft)"/>
    <g fill="none" stroke="var(--gold)" stroke-width="2.5">
      <circle cx="719" cy="265" r="19"/>
      <circle cx="719" cy="310" r="19"/>
      <circle cx="719" cy="354" r="19"/>
    </g>
    <g fill="none" stroke="var(--gold-light)" stroke-width="2.5" stroke-linecap="round" stroke-linejoin="round">
      <path d="M712,262 l5,8 l9,-12"/>
      <path d="M712,307 l5,8 l9,-12"/>
      <path d="M712,351 l5,8 l9,-12"/>
    </g>
    <rect x="701" y="389" width="112" height="63" fill="var(--eu-green)"/>
  </svg>

  <div class="brand brand-top"><span class="dot"></span>KORNWIESE</div>
  <div class="brand brand-side"><span class="dot"></span>KORNWIESE</div>
  <div class="brand-vertical">KORNWIESE</div>

  <p class="t notice" style="top:392px">Dieses Produkt ist kein<br>Arzneimittel.</p>
  <p class="t notice" style="top:478px">zum Verzehr nicht<br>geeignet</p>

  <p class="t care" style="top:652px">Vor Anwendung gut schütteln.<br>Trocken, kühl und lichtgeschützt<br>lagern.</p>
  <p class="t care" style="top:741px">Nicht verwenden während der<br>Schwangerschaft und Stillzeit.</p>
  <p class="t care" style="top:808px">Außerhalb der Reichweite von<br>Kindern aufbewahren.</p>
  <p class="t care" style="top:874px">Vorsicht bei Hanfallergie.</p>
  <p class="t care" style="top:919px">Geöffnet mindestens<br>3 Monate haltbar.</p>

  <p class="t product-premium">Premium</p>
  <p class="t product-cbd">CBD</p>
  <p class="t product-oil">Hanföl</p>
  <p class="t strength">10%</p>
  <p class="t spectrum">Das volle<br>Spektrum der<br>Hanfpflanze.</p>

  <p class="t claim" style="top:252px">100 % Natürlich</p>
  <p class="t claim" style="top:297px">100 % Vegan</p>
  <p class="t claim" style="top:341px">100 % Glutenfrei</p>
  <ul class="bullets">
    <li>Biozertifiziert</li>
    <li>Voller Terpeneffekt</li>
    <li>Keine Konservierungsstoffe</li>
  </ul>
  <p class="t ingredients">Inhaltsstoffe:<br>Bio Hanfsamenöl<br>(kaltgepresst)<br>Bio Hanfsamenextrakt</p>

  <p class="t batch" style="top:988px">Charge:</p>
  <p class="t batch" style="top:1020px">Mindestens haltbar bis:</p>
  <div class="date-field"></div>
  <p class="t volume">10 ml</p>
</div>
</body>
</html>
```